HK-Steuerberatung WordPress Site fully implemented (tax advisor)

Hello!
I need a little Wordpress Site for my newly founded Tax-Advisor Company.
I am a one-man Office advising in the area of Crypto-Currency.
PLEASE only provide a Design, if you can also Implement a WP-Site afterwards on an existing Webspace.

Please find the Content and Website-Description in the attached Document

Language for the Website is German (for now)

Target Market(s)

Tax-Advisory (specialized in Crypto Currency)

Coding

Coded - Design and coding required

Number of Pages Required

5+ page

Font styles to use
Sans Serif

Requirements
Must have
• Wordpress Implementation afterwards - Details according to attached Project Information Document

```html
<!DOCTYPE html>
<html lang="de">
<head>
<meta charset="utf-8">
<title>Kollegendienst – HK Steuerberatung</title>
<link href="https://fonts.googleapis.com/css2?family=Manrope:wght@400;500;600;700;800&display=swap" rel="stylesheet">
<style>
  :root {
    --navy: #1b2a42;
    --navy-deep: #161d2b;
    --ink: #2f3440;
    --muted: #4a4f5a;
    --white: #ffffff;
    --line: #3a4458;
    --accent: #2e5aa8;
  }
  * { margin: 0; padding: 0; box-sizing: border-box; }
  html, body { width: 856px; height: 1200px; overflow: hidden; }
  body { font-family: "Manrope", sans-serif; color: var(--ink); background: var(--white); position: relative; }

  .topbar { position: absolute; left: 0; top: 0; width: 856px; height: 37px; background: var(--navy); color: var(--white); }
  .topbar .social { position: absolute; left: 71px; top: 13px; display: flex; gap: 10px; }
  .dot { width: 10px; height: 10px; border-radius: 50%; background: var(--white); display: block; }
  .topbar .contact { position: absolute; right: 71px; top: 11px; display: flex; gap: 13px; font-size: 11px; font-weight: 500; }
  .contact-item { display: flex; align-items: center; gap: 4px; }

  .header { position: absolute; left: 0; top: 37px; width: 856px; height: 64px; background: var(--white); }
  .brand { position: absolute; left: 71px; top: 22px; display: flex; align-items: center; gap: 6px; font-weight: 800; font-size: 13.5px; letter-spacing: 0.3px; color: var(--navy); }
  .brand .mark { width: 14px; height: 14px; background: var(--navy); display: block; }
  .nav { position: absolute; left: 383px; top: 0; height: 64px; display: flex; align-items: center; gap: 31px; font-size: 11px; font-weight: 500; color: var(--navy); }
  .nav .active { position: relative; }
  .nav .active::after { content: ""; position: absolute; left: 50%; top: 18px; width: 4px; height: 4px; margin-left: -2px; border-radius: 50%; background: var(--navy); }
  .btn-kontakt { position: absolute; left: 695px; top: 16px; width: 91px; height: 31px; border-radius: 15px 6px 15px 6px; background: var(--navy); color: var(--white); font-size: 11.5px; font-weight: 600; display: flex; align-items: center; justify-content: center; }

  .hero { position: absolute; left: 0; top: 101px; width: 856px; height: 164px; background: linear-gradient(100deg, #3b2f25 0%, #5c4532 35%, #6f6a63 60%, #a09d99 80%, #7d7a74 100%); }
  .hero::after { content: ""; position: absolute; inset: 0; background: rgba(20, 22, 30, 0.25); }
  .hero h1 { position: absolute; left: 0; right: 0; top: 66px; text-align: center; font-size: 28px; font-weight: 700; color: var(--white); z-index: 1; letter-spacing: -0.3px; }

  .intro { position: absolute; left: 71px; top: 314px; width: 715px; }
  .intro .lead { font-size: 11.2px; font-weight: 600; line-height: 21px; color: #3a3f4a; }
  .intro .body { margin-top: 4px; font-size: 10.8px; font-weight: 400; line-height: 20px; color: var(--muted); }

  .team-photo { position: absolute; left: 71px; top: 459px; width: 715px; height: 343px; border-radius: 24px; background: linear-gradient(90deg, #d8cfc3 0%, #c9ccd3 40%, #56627a 60%, #c8ccd2 85%, #9aa58f 100%); }

  .cta { position: absolute; left: 71px; top: 826px; width: 269px; height: 37px; border-radius: 18px 6px 18px 6px; background: var(--navy); color: var(--white); font-size: 12px; font-weight: 600; display: flex; align-items: center; padding-left: 19px; gap: 7px; }

  .footer { position: absolute; left: 0; top: 927px; width: 856px; height: 273px; background: var(--navy-deep); color: var(--white); }
  .footer .brand { left: 71px; top: 55px; color: var(--white); font-size: 15px; }
  .footer .brand .mark { background: var(--white); width: 16px; height: 16px; }
  .footer .about { position: absolute; left: 71px; top: 96px; width: 220px; font-size: 11px; line-height: 18px; color: #d6d9df; }
  .footer .social { position: absolute; left: 71px; top: 176px; display: flex; gap: 14px; }
  .footer .social .dot { width: 12px; height: 12px; }
  .divider { position: absolute; top: 55px; width: 1px; height: 148px; background: var(--line); }
  .divider::before { content: ""; position: absolute; left: -2px; top: 26px; width: 3px; height: 16px; background: var(--accent); }
  .col-title { position: absolute; top: 63px; font-size: 12px; font-weight: 700; }
  .links { position: absolute; left: 437px; top: 82px; list-style: none; font-size: 11.3px; line-height: 27.6px; color: #d6d9df; }
  .contact-list { position: absolute; left: 646px; top: 82px; list-style: none; font-size: 11.3px; line-height: 27.6px; color: #d6d9df; }
  .contact-list li { display: flex; align-items: center; gap: 8px; }
  .rule { position: absolute; left: 69px; top: 230px; width: 717px; height: 1px; background: var(--line); }
  .copyright { position: absolute; left: 0; right: 0; top: 245px; text-align: center; font-size: 10px; color: #d6d9df; }
  .copyright strong { color: var(--white); font-weight: 600; }
</style>
</head>
<body>
  <div class="topbar">
    <div class="social">
      <span class="dot" aria-label="Social-Media-Link"></span>
      <span class="dot" aria-label="Social-Media-Link"></span>
      <span class="dot" aria-label="Social-Media-Link"></span>
    </div>
    <div class="contact">
      <span class="contact-item">
        <svg width="11" height="11" viewBox="0 0 24 24" fill="#fff"><path d="M6.6 10.8a15.1 15.1 0 0 0 6.6 6.6l2.2-2.2a1 1 0 0 1 1-.25 11.4 11.4 0 0 0 3.6.57 1 1 0 0 1 1 1V20a1 1 0 0 1-1 1A17 17 0 0 1 3 4a1 1 0 0 1 1-1h3.5a1 1 0 0 1 1 1c0 1.25.2 2.45.57 3.57a1 1 0 0 1-.25 1z"/></svg>
        +43 512 000 417
      </span>
      <span class="contact-item">
        <svg width="12" height="10" viewBox="0 0 24 18" fill="#fff"><path d="M0 2a2 2 0 0 1 2-2h20a2 2 0 0 1 2 2v.5L12 10 0 2.5z"/><path d="M0 5l12 7.5L24 5v11a2 2 0 0 1-2 2H2a2 2 0 0 1-2-2z"/></svg>
        office@krypto-steuer.example
      </span>
    </div>
  </div>

  <header class="header">
    <div class="brand"><span class="mark"></span>HK STEUERBERATUNG</div>
    <nav class="nav">
      <span>Home</span>
      <span class="active">Leistungen</span>
      <span>Über mich</span>
      <span>Impressum</span>
    </nav>
    <div class="btn-kontakt">Kontakt</div>
  </header>

  <section class="hero" role="img" aria-label="Foto: Team am Besprechungstisch von oben, Büro mit Kakteen am Fenster">
    <h1>KOLLEGENDIENST</h1>
  </section>

  <section class="intro">
    <p class="lead">Ihr Fokus liegt in der traditionellen Steuerberatung und Sie haben keine Zeit sich das hochkomplexe Spezialthema Kryptowährungen etc. einzuarbeiten?</p>
    <p class="body">Um Ihre Klienten dennoch weiterhin vollumfänglich beraten zu können, biete ich Ihnen gerne mein Know-How und die gesamte Leistungspalette an um Ihre Kunden ganz nach Ihrem Wunsch entweder direkt oder diskret im Hintergrund bei sämtlichen Themen rund um Krypto mit steuerlicher Expertise dazu zu unterstützen.</p>
  </section>

  <div class="team-photo" role="img" aria-label="Foto: lächelndes Team aus fünf Berufstätigen im Büro"></div>

  <div class="cta">
    Nehmen sie gerne Kontakt mit mir auf!
    <svg width="11" height="11" viewBox="0 0 20 20"><circle cx="10" cy="10" r="10" fill="#fff"/><path d="M8 5.5l4.5 4.5L8 14.5" stroke="#1b2a42" stroke-width="2.6" fill="none" stroke-linecap="round" stroke-linejoin="round"/></svg>
  </div>

  <footer class="footer">
    <div class="brand"><span class="mark"></span>HK STEUERBERATUNG</div>
    <p class="about">Ihrem Spezialisten bei allen steuerlichen Themen rund um Einkünfte &amp; Vermögen aus Krypto-Assets.</p>
    <div class="social">
      <span class="dot" aria-label="Social-Media-Link"></span>
      <span class="dot" aria-label="Social-Media-Link"></span>
      <span class="dot" aria-label="Social-Media-Link"></span>
    </div>

    <div class="divider" style="left:367px"></div>
    <div class="divider" style="left:585px"></div>

    <h3 class="col-title" style="left:438px">QUICK LINKS</h3>
    <ul class="links">
      <li>Home</li>
      <li>Leistungen</li>
      <li>Über mich</li>
      <li>Impressum</li>
      <li>Kontakt</li>
    </ul>

    <h3 class="col-title" style="left:646px">CONTACT US</h3>
    <ul class="contact-list">
      <li>
        <svg width="12" height="9" viewBox="0 0 24 18" fill="#9aa1ad"><path d="M0 2a2 2 0 0 1 2-2h20a2 2 0 0 1 2 2v.5L12 10 0 2.5z"/><path d="M0 5l12 7.5L24 5v11a2 2 0 0 1-2 2H2a2 2 0 0 1-2-2z"/></svg>
        office@krypto-steuer.example
      </li>
      <li>
        <svg width="11" height="11" viewBox="0 0 24 24" fill="#9aa1ad"><path d="M6.6 10.8a15.1 15.1 0 0 0 6.6 6.6l2.2-2.2a1 1 0 0 1 1-.25 11.4 11.4 0 0 0 3.6.57 1 1 0 0 1 1 1V20a1 1 0 0 1-1 1A17 17 0 0 1 3 4a1 1 0 0 1 1-1h3.5a1 1 0 0 1 1 1c0 1.25.2 2.45.57 3.57a1 1 0 0 1-.25 1z"/></svg>
        +43 512 000 417
      </li>
    </ul>

    <div class="rule"></div>
    <p class="copyright">© 2022 <strong>HK-Steuerberatung</strong>. All right reserved</p>
  </footer>
</body>
</html>
```